New, modern business card for growing audiology practice

We need a new business card for our audiology practice. Our logo and website have recently changed (more modern) and we want our business cards to reflect this change.
We conduct hearing tests, perform earwax removals, and fit & dispense hearing aids to our patients. We are a family owned practice in which the owner is the one who works directly with the patient. I have attached logos in various formats to use, as well as two ideas I found on this website; as well as a scanned copy of our current logo. Good luck!

Industry/Entity Type

Business

Contact Information for Business Card

Company name: Maplow Hearing Center
Provider name: Peter Mulvoy, Au.D. F/ISN
Phone number: (555) 318-6042
Address: 87 W. Linden Ave. Brookhollow, OH 45870
email: maplowhearing@postvale.net
website: maplowhearing.com

Colors
000000
aaaaaa
dbdbdb
cacaca
9bcb3c
afd23c
cadf82
b1b1b1

Requirements
Must have
• My card must include information in the "details" section. In the attached images, I found a few that I liked and I would like to model after - "brisk tumblin'" and "Sound Wellness Center".
• Must be horizontal.
• Must include logos provided. I uploaded them in various file formats and various ways.
• Must match logo font, if possible, if not, please get as close as you can.
Nice to have
• I really like the idea of having a color on one side with just the logo and company name and the contact information and provider name on the other side. I also really like the idea of having the main color dominating on the logo/company side with accent of that same color on the contact side of the card.
Should not have
• Must not be vertical.

```html
<!DOCTYPE html>
<html lang="en">
<head>
<meta charset="utf-8">
<title>Maplow Hearing Center – Business Card</title>
<link href="https://fonts.googleapis.com/css2?family=Didact+Gothic&family=Montserrat:wght@600&display=swap" rel="stylesheet">
<style>
  :root {
    --card-black: #0b0b0b;
    --stage: #dbdbdb;
    --green: #9bcb3c;
    --green-bright: #afd23c;
    --text-light: #f2f2f2;
    --rule-grey: #aaaaaa;
  }
  * { box-sizing: border-box; margin: 0; padding: 0; }
  html, body { width: 1200px; height: 780px; overflow: hidden; }
  body {
    background: var(--stage);
    font-family: "Didact Gothic", "Century Gothic", sans-serif;
    display: flex;
    align-items: center;
    justify-content: center;
    gap: 50px;
  }
  .card {
    width: 525px;
    height: 300px;
    background: var(--card-black);
    border-radius: 18px;
    position: relative;
    color: var(--text-light);
  }
  /* Contact side */
  .brand-mark {
    position: absolute;
    left: 28px;
    top: 70px;
    width: 150px;
    display: flex;
    flex-direction: column;
    align-items: center;
    gap: 12px;
  }
  .brand-ring {
    width: 96px; height: 96px;
    border: 9px solid var(--green-bright);
    border-radius: 50%;
  }
  .brand-mark-name {
    color: var(--green-bright);
    font-size: 12px;
    letter-spacing: 1.5px;
    text-transform: uppercase;
    text-align: center;
    line-height: 1.4;
  }
  .divider {
    position: absolute;
    left: 196px;
    top: 50px;
    width: 1px;
    height: 200px;
    background: var(--rule-grey);
  }
  .contact {
    position: absolute;
    left: 222px;
    top: 62px;
    right: 20px;
  }
  .provider-name {
    font-family: "Montserrat", sans-serif;
    font-weight: 600;
    font-size: 15px;
    letter-spacing: 0.5px;
    text-transform: uppercase;
  }
  .provider-role {
    color: var(--green);
    font-size: 13px;
    margin-bottom: 6px;
  }
  .address { font-size: 13px; line-height: 1.45; margin-bottom: 6px; }
  .contact-list { list-style: none; }
  .contact-list li {
    display: flex;
    align-items: center;
    gap: 9px;
    font-size: 13px;
    margin-bottom: 5px;
  }
  .contact-icon { width: 20px; height: 20px; flex: none; }
  /* Logo side */
  .logo-lockup {
    position: absolute;
    inset: 0;
    display: flex;
    align-items: center;
    justify-content: center;
    gap: 14px;
  }
  .logo-dot {
    width: 24px; height: 24px;
    border: 4px solid var(--green);
    border-radius: 50%;
  }
  .logo-name {
    font-size: 26px;
    letter-spacing: 1px;
    text-transform: uppercase;
    color: var(--text-light);
  }
</style>
</head>
<body>
  <section class="card card-contact">
    <div class="brand-mark">
      <div class="brand-ring"></div>
      <div class="brand-mark-name">Maplow<br>Hearing Center</div>
    </div>
    <div class="divider"></div>
    <div class="contact">
      <p class="provider-name">Peter Mulvoy, Au.D. F/ISN</p>
      <p class="provider-role">Owner/ audiologist</p>
      <p class="address">87 W. Linden Ave.<br>Brookhollow, OH 45870</p>
      <ul class="contact-list">
        <li>
          <svg class="contact-icon" viewBox="0 0 20 20" aria-hidden="true">
            <circle cx="10" cy="10" r="9" fill="none" stroke="#9bcb3c" stroke-width="1.5"/>
            <path d="M6.5 7.5c0 3 3 6 6 6l1-1.6-1.8-1-1 .8c-1-.5-1.9-1.4-2.4-2.4l.8-1-1-1.8z" fill="#9bcb3c"/>
          </svg>
          (555) 318-6042
        </li>
        <li>
          <svg class="contact-icon" viewBox="0 0 20 20" aria-hidden="true">
            <circle cx="10" cy="10" r="9" fill="none" stroke="#9bcb3c" stroke-width="1.5"/>
            <rect x="5.5" y="7" width="9" height="6.5" fill="none" stroke="#9bcb3c" stroke-width="1.3"/>
            <path d="M5.5 7l4.5 3.6L14.5 7" fill="none" stroke="#9bcb3c" stroke-width="1.3"/>
          </svg>
          maplowhearing@postvale.net
        </li>
        <li>
          <svg class="contact-icon" viewBox="0 0 20 20" aria-hidden="true">
            <circle cx="10" cy="10" r="9" fill="none" stroke="#9bcb3c" stroke-width="1.5"/>
            <circle cx="10" cy="10" r="5" fill="none" stroke="#9bcb3c" stroke-width="1.2"/>
            <ellipse cx="10" cy="10" rx="2.2" ry="5" fill="none" stroke="#9bcb3c" stroke-width="1"/>
            <path d="M5 10h10" stroke="#9bcb3c" stroke-width="1"/>
          </svg>
          www.maplowhearing.com
        </li>
      </ul>
    </div>
  </section>

  <section class="card card-logo">
    <div class="logo-lockup">
      <div class="logo-dot"></div>
      <p class="logo-name">Maplow Hearing Center</p>
    </div>
  </section>
</body>
</html>
```